Private Mortgage Bank needs a brochure designed.

We need a brochure designed for a new Private Mortgage Bank based in Maryland. We provide financing options for real estate investors who are purchasing or refinancing an investment property. Our website is v4harborlend (dot) com. We are rental property specialists. I will attach our current logo and the business card design we have.
Real Estate Investors
Finance

```html
<!DOCTYPE html>
<html lang="en">
<head>
<meta charset="utf-8">
<title>V4 Harbor Lend – Tri-fold Brochure</title>
<link href="https://fonts.googleapis.com/css2?family=Montserrat:ital,wght@0,400;0,500;0,600;0,700;1,400;1,500;1,600;1,700&family=Playball&display=swap" rel="stylesheet">
<style>
:root{
  --page:#ececec;
  --paper:#f4f4f4;
  --green:#3f9a24;
  --lime:#8ccf2c;
  --forest:#1f5a12;
  --deep:#123d0b;
  --ink:#1b1b1b;
  --muted:#3a3a3a;
}
*{margin:0;padding:0;box-sizing:border-box}
html,body{width:708px;height:1200px;overflow:hidden;background:var(--page);font-family:"Montserrat",sans-serif;color:var(--ink)}
.spread{position:absolute;left:18px;width:672px;height:486px;display:flex;box-shadow:0 8px 18px rgba(0,0,0,.18)}
.spread--back{top:70px}
.spread--inside{top:650px}
.panel{position:relative;width:224px;height:486px;background:var(--paper);overflow:hidden}
.panel + .panel{border-left:1px solid rgba(0,0,0,.06)}
.panel--green{background:linear-gradient(160deg,var(--green) 0%,#2f7d18 50%,var(--forest) 100%);color:#fff}
.swoosh{position:absolute;left:0;width:224px}
.photo{position:absolute;left:0;width:224px}
.t{position:absolute;left:8px;right:8px;text-align:center}
.heading-italic{font-style:italic;font-weight:600;color:var(--deep);font-size:14.5px}
.body-italic{font-style:italic;font-size:8.6px;line-height:1.35}
.banner{position:absolute;height:26px;display:flex;align-items:center}
.banner__bar{height:100%;background:linear-gradient(90deg,var(--green),var(--lime));clip-path:polygon(6% 0,100% 0,94% 100%,0 100%);color:#fff;display:flex;align-items:center;padding:0 18px}
.banner__slash{width:6px;height:100%;margin-left:3px;transform:skewX(-28deg)}
.slash-g{background:var(--lime)}
.slash-d{background:var(--ink)}
.brand-name{font-weight:600;font-size:15px;letter-spacing:.5px}
.brand-dot{display:inline-block;width:10px;height:10px;border-radius:50%;margin-right:6px;vertical-align:middle}
.contact{font-size:8.4px;line-height:1.6}
.contact svg{width:8px;height:8px;vertical-align:-1px;margin-right:4px;fill:#fff}
.step{position:absolute;left:12px;right:12px}
.step__head{display:flex;align-items:center;gap:8px}
.icon-box{width:18px;height:18px;background:var(--deep);display:flex;align-items:center;justify-content:center}
.icon-box i{width:7px;height:7px;border:1.2px solid #fff;border-radius:2px}
.step__title{font-size:6.6px;font-weight:600;line-height:1.25}
.step__title em{font-weight:400}
.step__text{font-size:5.6px;line-height:1.45;margin-top:8px}
.script{font-family:"Playball",cursive}
.c-item{position:absolute;left:80px;display:flex;align-items:center;gap:14px;font-size:8px;line-height:1.3}
</style>
</head>
<body>

<!-- BACK SIDE -->
<section class="spread spread--back">
  <!-- markets & mission -->
  <div class="panel">
    <p class="t heading-italic" style="top:36px">Primary Markets of Focus</p>
    <p class="t body-italic" style="top:68px;font-size:8px">V4 focuses on specific markets where rental property activity is very high and where we have a local presence.</p>
    <div class="photo" role="img" aria-label="Modern white villa with a blue swimming pool under a clear sky" style="top:122px;height:191px;background:linear-gradient(180deg,#3d6fc1 0%,#7aa7e0 45%,#d9d6cf 70%,#4aa6c8 100%)"></div>
    <svg class="swoosh" style="top:100px" viewBox="0 0 224 60" height="60" preserveAspectRatio="none">
      <path d="M0 0H224V10Q120 50 0 20Z" fill="var(--paper)"/>
      <path d="M0 20Q120 50 224 10V22Q120 66 0 34Z" fill="var(--green)"/>
      <path d="M0 34Q120 66 224 22V30Q120 74 0 42Z" fill="var(--lime)"/>
    </svg>
    <div class="banner" style="top:338px;left:22px">
      <div class="banner__bar" style="width:160px;font-style:italic;font-weight:600;font-size:14px;padding-left:26px">OUR MISSION</div>
      <div class="banner__slash slash-g"></div><div class="banner__slash slash-d"></div>
    </div>
    <p class="t body-italic" style="top:386px;font-size:10px;line-height:1.32">Improve the quality of life for those who face the greatest disparity, by exposing mortgage finance strategies that can be leveraged into mass net worth creation.</p>
  </div>

  <!-- lending & contact -->
  <div class="panel panel--green">
    <svg class="swoosh" style="top:0" viewBox="0 0 224 245" height="245" preserveAspectRatio="none">
      <path d="M0 0H90L224 165V245H0Z" fill="rgba(255,255,255,.08)"/>
    </svg>
    <p class="t" style="top:110px"><span class="brand-dot" style="background:#fff"></span><span class="brand-name">V4 HARBOR LEND</span></p>
    <p class="t" style="top:166px;font-size:7.6px;line-height:1.4">We finance these transactions using our capital; all underwriting is done in-house.</p>
    <p class="t" style="top:198px;font-size:8.8px;line-height:1.35">We have $100 million to lend, with our minimum loan amount being $150,000 and our maximum loan amount at $3 million.</p>
    <div class="photo" role="img" aria-label="Bright living room with a tan leather sofa and plants" style="top:244px;height:126px;background:linear-gradient(180deg,#e8e6e2 0%,#d5d0c8 45%,#b0713f 65%,#8d7b67 100%)"></div>
    <div class="t contact" style="top:384px">
      <div><svg viewBox="0 0 10 10"><path d="M2 0L4 2 3 3.5Q4.5 6 6.5 7L8 6 10 8 8.5 10Q3 9.5 0 2Z"/></svg>+1 (410) 555-0178</div>
      <div><svg viewBox="0 0 10 10"><circle cx="5" cy="5" r="4.2" fill="none" stroke="#fff" stroke-width="1"/><path d="M1 5H9M5 1V9" stroke="#fff" stroke-width=".8"/></svg>www.v4harborlend.com</div>
      <div><svg viewBox="0 0 10 10"><rect x="0.5" y="2" width="9" height="6" fill="none" stroke="#fff"/><path d="M0.5 2L5 6 9.5 2" fill="none" stroke="#fff"/></svg>tlane@v4harborlend.com</div>
      <div style="line-height:1.3"><svg viewBox="0 0 10 10"><path d="M5 0A3.5 3.5 0 0 1 8.5 3.5C8.5 6 5 10 5 10S1.5 6 1.5 3.5A3.5 3.5 0 0 1 5 0Z"/></svg>1840 Harbor Point Road Ste. B,<br>Annapolis, Maryland 21401</div>
    </div>
    <svg class="swoosh" style="bottom:0" viewBox="0 0 224 40" height="40" preserveAspectRatio="none">
      <path d="M0 8Q110 40 224 0V12Q110 46 0 22Z" fill="#fff"/>
      <path d="M0 22Q110 46 224 12V20Q110 54 0 30Z" fill="var(--lime)"/>
    </svg>
  </div>

  <!-- front cover -->
  <div class="panel" style="background:#fafafa">
    <div class="photo" role="img" aria-label="Light living room with a grey sofa, yellow cushions and a dining table" style="top:0;height:215px;background:linear-gradient(180deg,#f2f2f0 0%,#e6e6e4 45%,#a7a9ab 60%,#d9b24a 66%,#ececea 100%)"></div>
    <svg class="swoosh" style="top:180px" viewBox="0 0 224 60" height="60" preserveAspectRatio="none">
      <path d="M0 10Q120 40 224 0V60H0Z" fill="#fafafa"/>
      <path d="M0 10Q120 40 224 0V14Q120 56 0 26Z" fill="var(--green)"/>
      <path d="M0 26Q120 56 224 14V20Q120 64 0 32Z" fill="var(--lime)"/>
    </svg>
    <p class="t" style="top:345px;color:var(--ink)"><span class="brand-dot" style="background:var(--green)"></span><span class="brand-name">V4 HARBOR LEND</span></p>
    <p class="t" style="top:398px;font-weight:600;font-size:12px;color:var(--green)">V4 Harbor Lend, LLC</p>
    <p class="t body-italic" style="top:414px;font-size:9.4px;line-height:1.35">is a private mortgage bank exclusively focusing on financing rental properties.</p>
    <svg class="swoosh" style="bottom:0" viewBox="0 0 224 34" height="34" preserveAspectRatio="none">
      <path d="M0 14Q120 -6 224 22V34H0Z" fill="var(--green)"/>
      <path d="M0 10Q120 -10 224 18V26Q120 0 0 20Z" fill="var(--lime)"/>
    </svg>
  </div>
</section>

<!-- INSIDE -->
<section class="spread spread--inside">
  <!-- process -->
  <div class="panel">
    <svg class="swoosh" style="top:28px" viewBox="0 0 224 80" height="80" preserveAspectRatio="none">
      <path d="M0 50Q120 60 224 0V14Q120 78 0 66Z" fill="var(--lime)"/>
      <path d="M0 58Q120 72 224 10V22Q120 92 0 76Z" fill="var(--green)"/>
    </svg>
    <div class="banner" style="top:26px;left:22px;height:24px">
      <div class="banner__bar" style="width:150px;font-weight:500;font-size:12px;padding-left:18px">Start The Process</div>
      <div class="banner__slash slash-g"></div><div class="banner__slash slash-d"></div>
    </div>
    <p class="t script" style="top:108px;font-size:11.5px;color:var(--green);line-height:1.25">Secure your Financing Before<br>you go Shopping for a Property!</p>

    <div class="step" style="top:152px">
      <div class="step__head"><span class="icon-box"><i></i></span><p class="step__title">Complete Mortgage Application<br><em>Borrower Task_1</em></p></div>
      <p class="step__text">The mortgage application should only take about 10-15 minutes to complete. You will provide basic demographic and collateral information. However, it is essential that the mortgage application is completed thoroughly including all Schedule of Real Estate Owned sections.</p>
    </div>
    <div class="step" style="top:253px">
      <div class="step__head"><span class="icon-box"><i></i></span><p class="step__title">Upload Bank Statements &amp; Photo ID<br><em>Borrower Task_2</em></p></div>
      <p class="step__text">Once you complete the mortgage application, you will be prompted to upload 2-months bank statements and your photo ID. Have these ready! Please ensure that you have validated the ending balance in your bank statement to ensure you can document adequate cash to close/reserves.</p>
    </div>
    <div class="step" style="top:359px">
      <div class="step__head"><span class="icon-box"><i></i></span><p class="step__title">Credit Report Review<br><em>Corporate Task</em></p></div>
      <p class="step__text">You will pay and authorize us to order a soft tri-merge credit report so the processor can review your credit history for eligibility. The report costs $18.<br>During the Pre-Approval Review process, we are looking to ensure the borrower has an acceptable credit score with responsible tradeline history.</p>
    </div>
    <svg class="swoosh" style="bottom:0" viewBox="0 0 224 34" height="34" preserveAspectRatio="none">
      <path d="M0 10Q120 30 224 0V34H0Z" fill="var(--green)"/>
      <path d="M0 6Q120 26 224 -4V6Q120 36 0 14Z" fill="var(--lime)"/>
    </svg>
  </div>

  <!-- pre-approval -->
  <div class="panel">
    <svg class="swoosh" style="top:0" viewBox="0 0 224 50" height="50" preserveAspectRatio="none">
      <path d="M0 28Q100 0 224 0V0H0Z" fill="var(--green)"/>
      <path d="M0 0H224V0Q110 6 0 34Z" fill="var(--lime)"/>
      <path d="M0 34Q110 6 224 0V8Q110 14 0 42Z" fill="var(--green)"/>
    </svg>
    <p class="t" style="top:56px;font-size:8.4px;line-height:1.4;color:var(--green)">Our team will pre-approve your mortgage application within 60-minutes of you providing the necessary pre-approval documents.</p>
    <p class="t" style="top:104px;font-size:8.4px;line-height:1.4">Once you are pre-approved you will receive a Proof of Funds Letter and Term Sheet.</p>
    <div class="photo" role="img" aria-label="Two-storey white house with a driveway under a blue sky" style="top:142px;height:200px;background:linear-gradient(180deg,#2f73c9 0%,#79aee4 35%,#e8e6df 60%,#6a6560 80%,#5a8a3a 100%)"></div>
    <div style="position:absolute;top:360px;left:10px;width:206px;height:60px;border-radius:10px;background:linear-gradient(90deg,var(--green),var(--lime));color:var(--ink)">
      <span style="position:absolute;left:6px;top:-2px;font-size:18px;font-weight:700;color:var(--deep)">&ldquo;</span>
      <p class="script" style="position:absolute;left:10px;right:10px;top:9px;text-align:center;font-size:10.5px;line-height:1.25">We have strategic relationships that give us access to financing options which are difficult for individuals to find.</p>
      <span style="position:absolute;right:6px;bottom:-14px;font-size:18px;font-weight:700;color:var(--deep)">&rdquo;</span>
    </div>
    <p class="t" style="top:431px;font-size:10.5px;font-weight:600;color:var(--green)">Trevor Lane</p>
    <p class="t" style="top:447px;font-size:8.8px;line-height:1.35">V4 Commercial Mortgage<br>Founder | CEO</p>
  </div>

  <!-- underwriting -->
  <div class="panel">
    <svg class="swoosh" style="top:0" viewBox="0 0 224 70" height="70" preserveAspectRatio="none">
      <path d="M0 0H224V60Q120 0 0 2Z" fill="var(--forest)"/>
      <path d="M0 2Q120 0 224 60V64Q120 8 0 10Z" fill="#fff"/>
    </svg>
    <div class="banner" style="top:82px;left:22px;height:24px">
      <div class="banner__bar" style="width:150px;font-weight:600;font-size:10.5px;padding-left:14px">Underwriting Philosophy</div>
      <div class="banner__slash slash-g"></div><div class="banner__slash slash-d"></div>
    </div>
    <p class="t" style="top:114px;font-size:7.8px">3 C's — Credit | Cash | Collateral</p>
    <p class="t" style="top:140px;font-size:7.5px;line-height:1.4;left:6px;right:4px">We provide asset-based mortgage financing opportunities. We do not document the borrower's ability to repay the loan. Instead, we document the property's ability to secure the loan through cash flow or appreciation.</p>
    <div class="c-item" style="top:208px"><span class="icon-box"><i></i></span><span>Credit<br>| Soft-Pull</span></div>
    <div class="c-item" style="top:248px"><span class="icon-box"><i></i></span><span>Cash/Equity<br>| Assets</span></div>
    <div class="c-item" style="top:288px"><span class="icon-box"><i></i></span><span>Collateral<br>| Appraisal</span></div>
    <div class="photo" role="img" aria-label="Grey farmhouse with a white porch among trees on a green lawn" style="top:360px;height:126px;background:linear-gradient(180deg,#cfd9e3 0%,#9aa7b4 35%,#6b7280 55%,#4f7a2c 80%,#6ea13a 100%)"></div>
    <svg class="swoosh" style="top:318px" viewBox="0 0 224 60" height="60" preserveAspectRatio="none">
      <path d="M0 20Q120 -4 224 10V24Q120 6 0 34Z" fill="var(--lime)"/>
      <path d="M0 34Q120 6 224 24V34Q120 16 0 44Z" fill="var(--green)"/>
      <path d="M0 44Q120 16 224 34V36Q120 24 0 50Z" fill="var(--paper)"/>
    </svg>
  </div>
</section>

</body>
</html>
```